Web design for new streaming audio service

We need a homepage design for a new streaming audio service. Our company is called Lumawave, and we’re basically Reelcove for Audiobooks, Stand-Up Comedy, Lectures, Language Learning, etc. Essentially like Tunevast for everything audio EXCEPT music.
You don’t have to code the homepage (Design Only), but it should include 3 different designs to work with 1) Web; 2) Phones; 3) Tablets.
Below is a link to a mockup of the web version which gives a good idea of what elements we want. This is just a mockup and we want you to improve it.
Once you download the mockup, please refer to the more detailed instructions below:
The following outlines the design project for the Lumawave homepage. We have provided a rough mockup of the homepage layout that gives you a general idea of what we’re going for. There are a few elements that we are attached to, and many others where you have complete creative freedom to do whatever you think looks good.
The ZIP file includes the following:
* Mockup to see what we have in mind (lumawave-homepage-mockup.jpg)
* Text used (lumawave-homepage-text.txt)
* Raw image of actor (lumawave-actor1.jpg)
* Raw images for samples (lumawave-sample-[name].jpg)
Although we have only provided a mockup layout for the web version, we also need you to provide a mobile phone and a tablet version of the design also. It’s very possible the tablet version may be substantially similar to the web version, but the mobile phone version will likely be much different.
All of the raw files are included in the attached ZIP file. Please use our photographs and text as provided although cropping, sizing, etc. is flexible per the instructions below.
Display Requirements:
* Web Version - Minimum resolution 1024x768 (72 dpi) but should look good on 1920x1080 (72 dpi) - Page should be designed to scale to look acceptable in all resolutions in between.
* Phone Version - Minimum Zelphone 4 - 640x960 (326 dpi) but should look good on Ordano Vexa T3 - 1920x1080 (441 dpi) - Page should be designed to scale to look acceptable in all resolutions and devices in between.
* Tablet Version - Minimum Pagelit Ember QX 7” - 1280x800 (216 dpi) but should also look good on a Tabrel Wisp - 2048x1536 (264 dpi) - Page should be designed to scale to look acceptable in all resolutions and devices in between.
Above the Fold - We want to make sure the Lumawave logo, Member Login Link, Large Photo, Headline, Price, Button, and the first row of sample images are all “Above the fold”. As a general guideline, this means 600 pixels high on a 1024x768 72 dpi web screen. This requirement is less important on Phone versions.
Top Logo Bar - We want to retain the blue bar with the Lumawave logo on the page, although we are open to a different size, shape and positioning if it greatly enhances the design. Please use the standard logo color, although you are welcome to use either the horizontal or vertical orientation of the logo based on your design.
Text color, font and size - Feel free to design the text in anyway you choose as long as the text is readable on the target platforms.
Buttons - Feel free to use any size, shape and colors for the buttons as long as they are obvious and clickable relative to the page. The only exception is the Chatterly button should follow the Chatterly color scheme and logo treatment (the mockup doesn’t seem 100% correct.)
Top Photograph - We want to retain the large photograph across the top of the screen although final shape and dimensions are flexible.
Size and shape of content samples (i.e. Audiobooks, Stand-Up Comedy, etc.) - Feel free to design the content samples in anyway you choose.
Three Sales Points (i.e. Listen on your Zelphone…, All you can enjoy…, etc.) - The Three Sales Points are envisioned to each have a corresponding illustration which you should provide and have rights for. The placeholder is represented by a square next to the text. The color size and shape of these elements are flexible and can be designed in any way you choose.
Opt-in form - Feel free to design the opt-in form in anyway you choose as long as the text is readable and the interactivity is obvious on the target platforms.
Text links and copyright notice - Feel free to design the bottom of the page text links and copyright notice in anyway you choose.
Additional colors, graphic design elements, etc. - Feel free to use any additional colors, graphic design elements, etc. to support your design.
Target Market(s)
people who want to listen to audio through their mobile devices.
Industry/Entity Type
Graphic Design
Look and feel

```html
<!DOCTYPE html>
<html lang="en">
<head>
<meta charset="utf-8">
<title>Lumawave – Unlimited Listening</title>
<link rel="stylesheet" href="https://fonts.googleapis.com/css2?family=Arimo:ital,wght@0,400;0,700;1,400&family=Cinzel:wght@400&display=swap">
<style>
:root{
  --topbar:#0d2637;
  --sky-top:#29b2e6;
  --sky-bottom:#0a7cbf;
  --navy:#1a3d78;
  --price-blue:#1567c9;
  --cyan-note:#14b3e6;
  --gold-top:#f2b431;
  --gold-bottom:#c9820c;
  --cta-text:#6e1208;
  --cream:#f9f8f2;
  --label:#1b2634;
  --orange-head:#c9870e;
  --body-grey:#3c3c3c;
  --footer:#262626;
  --footer-text:#d6d6d6;
  --chatterly:#5a6fb6;
}
*{margin:0;padding:0;box-sizing:border-box}
html,body{width:1200px;height:1054px;overflow:hidden;background:#fff}
body{font-family:"Arimo",Arial,sans-serif;position:relative}
.abs{position:absolute}

.top-bar{left:0;top:0;width:1200px;height:16px;background:var(--topbar)}
.top-bar .account{left:818px;top:1px;font-size:11px;color:#9fb3c0;display:flex;align-items:center;gap:6px}
.top-bar .account svg{width:10px;height:10px}

.brand-bar{left:0;top:16px;width:1200px;height:58px;background:linear-gradient(var(--sky-top),var(--sky-bottom))}
.logo{left:168px;top:13px;display:flex;align-items:center;gap:10px;color:#fff;font-size:30px;font-weight:400}
.logo .dot{width:30px;height:30px;border-radius:50%;background:#fff}
.members-login{left:816px;top:20px;width:132px;height:26px;border-radius:4px;
  background:linear-gradient(#f7c545,#d08d12);border:1px solid #7a4a06;
  color:#3a1a04;font-size:12px;font-weight:700;display:flex;align-items:center;justify-content:center;gap:6px}
.members-login svg{width:12px;height:12px}

.hero{left:0;top:74px;width:1200px;height:258px;background:#fff}
.hero-photo{left:149px;top:0;width:601px;height:258px;
  background:linear-gradient(100deg,#4a4a4a 0%,#8d8d8d 35%,#c9c9c9 65%,#f2f2f2 100%)}
.headline{font-family:"Cinzel",Georgia,serif;color:var(--navy);font-size:34px;line-height:40px;font-weight:400;white-space:nowrap}
.headline .l1{position:absolute;left:578px;top:40px}
.headline .l2{position:absolute;left:632px;top:80px}
.price{left:600px;top:134px;width:440px;text-align:center;font-size:23px;color:var(--price-blue)}
.trial-btn{left:707px;top:177px;width:284px;height:50px;border-radius:6px;border:1px solid #8a5a08;
  background:linear-gradient(var(--gold-top),var(--gold-bottom));color:var(--cta-text);
  font-size:25px;font-weight:700;display:flex;align-items:center;justify-content:center}
.card-note{left:760px;top:229px;width:224px;text-align:right;font-size:11px;color:var(--cyan-note)}
.hero-rule{left:0;top:332px;width:1200px;height:4px;background:var(--topbar)}

.catalogue{left:0;top:336px;width:1200px;height:408px;background:var(--cream);border-bottom:1px solid #888}
.sample{display:flex;align-items:center;gap:26px}
.sample .thumb{width:110px;height:98px;background:#fff;border-radius:8px;padding:7px;
  box-shadow:0 2px 6px rgba(0,0,0,.35)}
.sample .thumb span{display:block;width:100%;height:100%}
.sample .label{font-size:15.5px;font-weight:700;color:var(--label);line-height:18px}
.read-more{left:786px;top:365px;width:126px;height:38px;border-radius:19px;
  background:linear-gradient(#36c7e4,#0f8fb8);border:1px solid #0a6e8c;color:#fff;
  font-size:13px;font-style:italic;display:flex;align-items:center;justify-content:flex-end;gap:8px;padding-right:6px}
.read-more svg{width:28px;height:28px}

.signup{left:0;top:744px;width:1200px;height:216px;background:#fff;border-left:1px solid #aaa;border-right:1px solid #aaa}
.signup h2{left:157px;top:28px;font-size:24px;font-weight:700;color:var(--orange-head)}
.signup .pitch{left:157px;top:58px;width:290px;font-size:11.5px;font-weight:700;color:var(--body-grey);line-height:14px;white-space:nowrap}
.signup .fine{left:157px;top:162px;font-size:12px;font-weight:700;color:var(--body-grey)}
.btn{width:239px;border-radius:4px;color:#fff;font-size:18px;font-weight:700;display:flex;align-items:center;justify-content:center}
.btn-access{left:458px;top:28px;height:43px;background:linear-gradient(#5a5a5a,#111);border:1px solid #000}
.btn-chatterly{left:458px;top:104px;height:44px;background:var(--chatterly);border:1px solid #2c3a78}
.email{left:727px;top:31px;width:291px;height:34px;border:2px solid #5aa7e0;border-radius:3px;
  font-size:13px;color:#a9a9a9;padding:8px 12px;letter-spacing:.5px}
.subscribe{left:840px;top:74px;height:33px;width:169px;display:flex;border-radius:4px;overflow:hidden;
  font-size:16px;font-weight:700;color:#fff}
.subscribe .a{flex:0 0 112px;background:linear-gradient(#4aa2e8,#1c6cc0);display:flex;align-items:center;justify-content:center}
.subscribe .b{flex:1;background:linear-gradient(#f06a3a,#cc3a12);display:flex;align-items:center;justify-content:center}

.site-footer{left:0;top:960px;width:1200px;height:94px;background:var(--footer)}
.site-footer nav{left:156px;top:34px;font-size:12.5px;color:var(--footer-text)}
.site-footer small{left:162px;top:62px;font-size:9.5px;color:var(--footer-text)}
</style>
</head>
<body>

<header>
  <div class="abs top-bar">
    <div class="abs account">
      <svg viewBox="0 0 10 10"><circle cx="5" cy="3" r="2.3" fill="#5fb0e0"/><path d="M1 10a4 4 0 0 1 8 0z" fill="#5fb0e0"/></svg>
      <span>Welcome &nbsp;| Register new User</span>
    </div>
  </div>
  <div class="abs brand-bar">
    <div class="abs logo"><span class="dot"></span>Lumawave</div>
    <div class="abs members-login">
      <svg viewBox="0 0 12 12"><path d="M8 2 3 6l5 4z" fill="#7a2a08"/></svg>
      Members Login
      <svg viewBox="0 0 12 12"><path d="M4 2l5 4-5 4z" fill="#7a2a08"/></svg>
    </div>
  </div>
</header>

<section class="abs hero">
  <div class="abs hero-photo" role="img" aria-label="Black and white photo of a smiling man wearing headphones, looking at his phone"></div>
  <h1 class="headline"><span class="l1">Unlimited Listening</span><span class="l2">Wherever you are</span></h1>
  <p class="abs price">Only $9.99 per month</p>
  <div class="abs trial-btn">Start Your Free Trial</div>
  <p class="abs card-note">* Credit Card Not Required</p>
</section>
<div class="abs hero-rule"></div>

<section class="abs catalogue">
  <div class="abs sample" style="left:156px;top:72px">
    <div class="thumb"><span role="img" aria-label="Audiobook cover art" style="background:linear-gradient(#3d5566,#1c2a33)"></span></div>
    <div class="label" style="margin-left:2px">Audiobooks</div>
  </div>
  <div class="abs sample" style="left:448px;top:70px">
    <div class="thumb"><span role="img" aria-label="Stand-up comedy album cover" style="background:linear-gradient(#b9a9a0,#7c6a64)"></span></div>
    <div class="label" style="margin-left:2px">Stand-Up<br>Comedy</div>
  </div>
  <div class="abs sample" style="left:786px;top:72px">
    <div class="thumb"><span role="img" aria-label="Biography and memoir program cover" style="background:linear-gradient(#5a1a12,#1f0a08)"></span></div>
    <div class="label" style="margin-left:-12px">Biography &amp;<br>Memoirs</div>
  </div>
  <div class="abs sample" style="left:151px;top:234px">
    <div class="thumb"><span role="img" aria-label="Celebrity interview cover" style="background:linear-gradient(#7a4a2a,#3e2418)"></span></div>
    <div class="label" style="margin-left:-1px">Celebrity<br>Interviews</div>
  </div>
  <div class="abs sample" style="left:449px;top:234px">
    <div class="thumb"><span role="img" aria-label="Fitness program cover" style="background:linear-gradient(#48b4e6,#e0584a)"></span></div>
    <div class="label" style="margin-left:8px">Fitness<br>Programs</div>
  </div>
  <div class="abs sample" style="left:787px;top:234px">
    <div class="thumb"><span role="img" aria-label="Business training program cover" style="background:linear-gradient(#6a2414,#1e0a06)"></span></div>
    <div class="label" style="margin-left:-11px">Business<br>Training</div>
  </div>
  <div class="abs read-more">READ MORE
    <svg viewBox="0 0 28 28"><circle cx="14" cy="14" r="13" fill="#1b3346"/><path d="M11 8l9 6-9 6z" fill="#fff"/></svg>
  </div>
</section>

<section class="abs signup">
  <h2 class="abs">Start Your Free Trial</h2>
  <p class="abs pitch">You Will Get Instant &amp; Unlimited access<br>to all the material on Lumawave for 14 days.<br>There is no obligation &amp; you can cancel<br>at any time</p>
  <p class="abs fine">Credit Card Not Required for Free Trial</p>
  <div class="abs btn btn-access">Get Instant Access</div>
  <div class="abs btn btn-chatterly">Sign Up Using Chatterly</div>
  <div class="abs email">ENTER YOUR EMAIL</div>
  <div class="abs subscribe"><span class="a">SUBSCRIBE</span><span class="b">NOW</span></div>
</section>

<footer class="abs site-footer">
  <nav class="abs">About | Help | Contact Us | Member Login | Privacy Policy | Terms of Service</nav>
  <small class="abs">© 2014 Lumawave LLC - All Rights Reserved</small>
</footer>

</body>
</html>
```